Webdesign for a Bikeshop in Innsbruck (female audience)

To obtain my master's degree, I am conducting a study in the field of web design as part of my master thesis. All submitted designs will therefore be used for study purposes. In order to achieve a homogeneous group, I would like to encourage not only male but also female web designers to submit a design. All submitted designs will be used anonymously for the study and therefore do not allow any conclusions to be drawn about your person. Since this is a contest, the winner will be chosen randomly from all serious submissions. I would be really happy if you would support me in my study. I think the results could be very informative and also useful for your further work (I won't go into more detail here as it could skew the results - but once the contest is over, feel free to contact me. Of course I will also provide you with my results as soon as my work is finished). Below you will find a fictitious usecase and a description of what the website should include:

The company Bikeshop Valdorna is planning to relaunch its own website and would like to present itself primarily as a competent and leading consultant in the field of cargo bikes. The design should appeal to a broad audience and embody an urban lifestyle. In any case, the website should include a landing page, a product overview page and a product details page. The company also wants to appeal mainly to a FEMALE target group. You only design the website. So don't worry about hardware or software limitations, just create the best bike store design you can.

As it is fictitious, I can't offer any materials. A logo is not necessary, you can use a placeholder or whatever you have access to. If you need any inspring websites feel free to contact me.

Target Market(s)

female users

Number of Pages Required

1 page

Requirements
Must have
• landing page, product overview page, product details page
Should not have
• online shop

```html
<!DOCTYPE html>
<html lang="en">
<head>
<meta charset="utf-8">
<title>Valdorna – Cargo Bike Consultants</title>
<link href="https://fonts.googleapis.com/css2?family=Poppins:wght@300;400;500;600;700&display=swap" rel="stylesheet">
<style>
:root{
  --olive:#515e2e;
  --ink:#1b1b1b;
  --muted:#6f6f6f;
  --line:#e6e6e6;
  --dark:#171717;
  --white:#ffffff;
  --star:#e9b21a;
}
*{margin:0;padding:0;box-sizing:border-box}
html,body{width:1200px;height:5380px;overflow:hidden;background:var(--white)}
body{font-family:"Poppins",sans-serif;color:var(--ink);position:relative}
.abs{position:absolute}
section,header,footer{position:absolute;left:0;width:1200px}

/* header */
.site-header{top:0;height:88px;background:var(--white)}
.brand{left:24px;top:24px;font-size:30px;font-weight:700;letter-spacing:1px;line-height:40px}
.main-nav{left:395px;top:34px;display:flex;gap:40px;font-size:13px;font-weight:500;letter-spacing:.5px}
.header-icons{left:1080px;top:32px;display:flex;gap:20px}

/* hero */
.hero{top:88px;height:640px;background:linear-gradient(100deg,#1c2017 0%,#3a3f33 35%,#6b6a60 60%,#3e3f37 100%)}
.hero-label{left:24px;top:178px;color:#fff;font-size:13px;font-weight:500;letter-spacing:.5px}
.hero-title{left:22px;top:200px;color:#fff;font-size:58px;font-weight:600;line-height:1.07}
.hero-text{left:24px;top:334px;color:#eee;font-size:15px;line-height:1.5;width:440px}
.btn{display:inline-block;font-size:12px;font-weight:500;letter-spacing:.5px;text-align:center}
.btn-light{left:52px;top:420px;width:150px;height:46px;line-height:46px;background:#fff;color:var(--ink)}
.btn-outline{left:232px;top:420px;width:144px;height:46px;line-height:44px;border:1px solid #fff;color:#fff}
.dots{display:flex;gap:8px}
.dot{width:9px;height:9px;border-radius:50%;background:rgba(255,255,255,.5)}
.dot.on{background:#fff}
.hero .dots{left:580px;top:608px}

/* headings */
.rule{width:70px;height:4px;background:var(--olive)}
.h-section{font-size:48px;font-weight:600;line-height:1.18}
.para{font-size:13px;line-height:1.7;color:var(--muted)}

/* about */
.about{top:728px;height:560px}
.photo-frame{border:1.5px solid #cfcfcf;border-radius:0 48px 0 48px}
.photo{border-radius:0 44px 0 44px}
.about .photo-frame{left:60px;top:70px;width:500px;height:452px}
.about .photo{left:28px;top:92px;width:520px;height:430px;background:linear-gradient(135deg,#c7cdbf,#5a5f50 55%,#2b2d27)}
.about .rule{left:628px;top:70px}
.about .h-section{left:628px;top:86px}
.about .para.lead{left:628px;top:160px;width:540px}
.feature{left:628px;width:540px;display:flex;gap:28px}
.feature-icon{width:56px;height:56px;border:1px solid #cfcfcf;display:flex;align-items:center;justify-content:center;flex:none}
.feature h3{font-size:20px;font-weight:500;margin-bottom:6px}
.btn-olive{background:var(--olive);color:#fff;height:52px;line-height:52px}
.about .btn-olive{left:628px;top:466px;width:160px}

/* products */
.products{top:1288px;height:872px}
.products .rule{left:20px;top:48px}
.products .h-section{left:20px;top:62px}
.tabs{left:20px;top:168px;display:flex;gap:14px}
.tab{height:34px;line-height:32px;padding:0 18px;border:1px solid #bdbdbd;font-size:11px;font-weight:500;letter-spacing:.4px}
.tab.active{background:var(--olive);border-color:var(--olive);color:#fff}
.product-grid{left:16px;top:252px;display:grid;grid-template-columns:292px 292px 576px;grid-template-rows:290px 290px;border-top:1px solid var(--line);border-left:1px solid var(--line)}
.card{position:relative;border-right:1px solid var(--line);border-bottom:1px solid var(--line);text-align:center}
.card.big{grid-column:3;grid-row:1/3}
.badge-new{position:absolute;left:18px;top:16px;background:var(--olive);color:#fff;font-size:10px;padding:3px 10px}
.bike{position:absolute;left:40px;top:56px;width:212px;height:150px;border-radius:6px;background:radial-gradient(ellipse at center,#7a8890 0%,#cfd4d7 55%,#f4f5f5 78%)}
.card.big .bike{left:90px;top:110px;width:400px;height:300px;background:radial-gradient(ellipse at center,#8b2c28 0%,#54504d 35%,#dcdcdc 65%,#fafafa 80%)}
.card-name{position:absolute;left:0;width:100%;top:218px;font-size:14px}
.card-price{position:absolute;left:0;width:100%;top:242px;font-size:14px;font-weight:500}
.card.big .card-name{top:440px}
.card.big .card-price{top:464px}

/* testimonial */
.testimonial{top:2160px;height:730px}
.testimonial .photo-frame{left:160px;top:80px;width:370px;height:540px;border-radius:0 60px 0 60px}
.testimonial .photo{left:112px;top:110px;width:404px;height:530px;border-radius:0 56px 0 56px;background:linear-gradient(160deg,#b8c8d6,#8b8d7a 45%,#7b6b57)}
.testimonial .rule{left:628px;top:170px}
.testimonial .h-section{left:628px;top:186px;font-size:46px}
.testimonial .para{left:628px;top:340px;width:500px}
.client-name{left:628px;top:412px;font-size:22px;font-weight:500;color:var(--olive)}
.client-role{left:628px;top:448px;font-size:10px;color:var(--muted);letter-spacing:.4px}
.stars{left:628px;top:466px}
.testimonial .dots{left:628px;top:502px}
.testimonial .dot{background:#ccc;width:7px;height:7px}
.testimonial .dot.on{background:var(--ink)}

/* banner */
.banner{top:2890px;height:640px;background:linear-gradient(110deg,#4a4c46 0%,#8c8b84 30%,#3d3b36 60%,#1e1f1c 100%)}
.banner-word{left:-6px;font-size:132px;font-weight:700;letter-spacing:4px;color:transparent;-webkit-text-stroke:1.5px rgba(255,255,255,.35);line-height:1}
.play{left:560px;top:280px;width:62px;height:62px;border-radius:50%;background:rgba(255,255,255,.85);display:flex;align-items:center;justify-content:center}

/* blog */
.blog{top:3530px;height:1030px}
.blog .h-section{left:16px;top:80px;font-size:46px}
.post{position:absolute}
.post-img{width:100%;position:relative}
.post-tag{position:absolute;left:50%;transform:translateX(-50%);bottom:0;background:var(--olive);color:#fff;font-size:10px;padding:5px 14px;white-space:nowrap}
.post-title{font-size:15px;font-weight:500;margin-top:10px}
.post-meta{font-size:10px;color:var(--muted);margin-top:6px;display:flex;gap:14px;letter-spacing:.3px}
.post.big{text-align:center}
.post.big .post-meta{justify-content:center}

/* highlights */
.highlights{top:4560px;height:400px;background:linear-gradient(180deg,#1d1f1b,#2f332c 50%,#1a1b18)}
.highlight{position:absolute;top:100px;width:330px;text-align:center;color:#fff}
.highlight h4{font-size:13px;font-weight:600;letter-spacing:.6px;margin:16px 0 8px}
.highlight p{font-size:12px;line-height:1.6;color:#d6d6d6}

/* footer */
.site-footer{top:4960px;height:420px;background:var(--dark);color:#fff}
.f-col{position:absolute;top:50px}
.f-col h5{font-size:13px;font-weight:600;letter-spacing:.5px;margin-bottom:20px}
.f-col ul{list-style:none}
.f-col li{font-size:11px;color:#cfcfcf;line-height:24px}
.f-col p{font-size:11px;color:#cfcfcf;line-height:1.6;width:300px}
.socials{display:flex;gap:10px;margin-top:22px}
.socials span{width:26px;height:26px;border-radius:50%;border:1px solid #bbb}
.footer-bottom{left:0;top:340px;width:1200px;height:80px;border-top:1px solid #2c2c2c}
.footer-brand{left:16px;top:22px;font-size:26px;font-weight:700;letter-spacing:1px}
.copyright{left:0;width:1200px;top:34px;text-align:center;font-size:11px;color:#bdbdbd}
.footer-links{right:20px;top:34px;display:flex;gap:28px;font-size:11px;color:#ddd}
</style>
</head>
<body>

<header class="site-header">
  <div class="abs brand">VALDORNA</div>
  <nav class="abs main-nav"><span>HOME</span><span>BIKES</span><span>ADVICE</span><span>BLOG</span><span>CONTACT US</span></nav>
  <div class="abs header-icons">
    <svg width="18" height="18" viewBox="0 0 18 18" fill="none" stroke="#1b1b1b" stroke-width="1.5"><circle cx="9" cy="6" r="3.5"/><path d="M2 17c1-4 4-6 7-6s6 2 7 6"/></svg>
    <svg width="18" height="18" viewBox="0 0 18 18" fill="none" stroke="#1b1b1b" stroke-width="1.5"><circle cx="8" cy="8" r="5.5"/><path d="M12 12l5 5"/></svg>
  </div>
</header>

<section class="hero" role="img" aria-label="Woman riding a cargo bike along a city street">
  <div class="abs hero-label">URBAN CARGO BIKE EXPERTS</div>
  <h1 class="abs hero-title">Plan the cycling<br>trip of a lifetime</h1>
  <p class="abs hero-text">Expert advice on cargo bikes for kids, groceries and daily city life</p>
  <a class="abs btn btn-light">EXPLORE BIKES</a>
  <a class="abs btn btn-outline">BOOK ADVICE</a>
  <div class="abs dots"><span class="dot on"></span><span class="dot"></span></div>
</section>

<section class="about">
  <div class="abs photo-frame"></div>
  <div class="abs photo" role="img" aria-label="Rider beside a cargo bike in the city"></div>
  <div class="abs rule"></div>
  <h2 class="abs h-section">About Us</h2>
  <p class="abs para lead">Valdorna is your leading consultant for cargo bikes – strong, safe and comfortable for school runs, shopping and work.</p>
  <div class="abs feature" style="top:250px">
    <div class="feature-icon"><svg width="28" height="28" viewBox="0 0 28 28" fill="none" stroke="#1b1b1b" stroke-width="1.4"><path d="M4 24l6-14 6 8 4-6 4 12z"/><path d="M10 4v6M10 4l6 2-6 2"/></svg></div>
    <div><h3>We Provide the Best Guide For you</h3><p class="para">Personal test rides and honest advice to find the cargo bike that fits your life</p></div>
  </div>
  <div class="abs feature" style="top:350px">
    <div class="feature-icon"><svg width="28" height="28" viewBox="0 0 28 28" fill="none" stroke="#1b1b1b" stroke-width="1.4"><path d="M14 3l11 21H3z"/><path d="M9 18h10"/></svg></div>
    <div><h3>Our targets</h3><p class="para">Making car-free city living easy, stylish and fun for every family</p></div>
  </div>
  <a class="abs btn btn-olive">READ MORE</a>
</section>

<section class="products">
  <div class="abs rule"></div>
  <h2 class="abs h-section">Featured Cargo Bikes</h2>
  <div class="abs tabs"><span class="tab active">FAMILY CARGO</span><span class="tab">LONG TAIL</span><span class="tab">ELECTRIC CARGO</span><span class="tab">COMPACT</span></div>
  <div class="abs product-grid">
    <div class="card"><span class="badge-new">New</span><div class="bike" role="img" aria-label="Blue front-box cargo bike"></div><div class="card-name">Ridgeline Cargo 8</div><div class="card-price">from €3,499</div></div>
    <div class="card"><span class="badge-new">New</span><div class="bike" role="img" aria-label="Black and red long-tail cargo bike" style="background:radial-gradient(ellipse at center,#8a3a2e 0%,#cfd0d0 55%,#f4f5f5 78%)"></div><div class="card-name">Ridgeline Cargo 7</div><div class="card-price">from €3,299</div></div>
    <div class="card big"><span class="badge-new">New</span><div class="bike" role="img" aria-label="Red electric cargo bike with child box"></div><div class="card-name">Summit Cargo 9</div><div class="card-price">from €4,999</div></div>
    <div class="card"><div class="bike" role="img" aria-label="Black compact cargo bike" style="background:radial-gradient(ellipse at center,#3c3c3c 0%,#cfcfcf 55%,#f4f5f5 78%)"></div><div class="card-name">Tundra Cargo 5</div><div class="card-price">from €2,899</div></div>
    <div class="card"><div class="bike" role="img" aria-label="Orange electric cargo bike" style="background:radial-gradient(ellipse at center,#c75a24 0%,#d6d2cf 55%,#f4f5f5 78%)"></div><div class="card-name">Ridgeline Cargo 6</div><div class="card-price">from €3,199</div></div>
  </div>
</section>

<section class="testimonial">
  <div class="abs photo-frame"></div>
  <div class="abs photo" role="img" aria-label="Smiling customer with her cargo bike"></div>
  <div class="abs rule"></div>
  <h2 class="abs h-section">That's what our<br>Client say</h2>
  <p class="abs para">The team took time to understand my daily routes and found the perfect cargo bike for me and my two kids.</p>
  <div class="abs client-name">Mara Stein</div>
  <div class="abs client-role">MOTHER &amp; COMMUTER</div>
  <div class="abs stars">
    <svg width="80" height="14" viewBox="0 0 80 14" fill="#e9b21a"><g id="s"><path d="M7 0l2 4.6 5 .5-3.8 3.3 1.1 5L7 10.8 2.7 13.4l1.1-5L0 5.1l5-.5z"/></g><use href="#s" x="16"/><use href="#s" x="32"/><use href="#s" x="48"/><use href="#s" x="64"/></svg>
  </div>
  <div class="abs dots"><span class="dot on"></span><span class="dot"></span></div>
</section>

<section class="banner" role="img" aria-label="Cargo bike rider on an urban route">
  <div class="abs banner-word" style="top:40px">ROAD</div>
  <div class="abs banner-word" style="top:200px">BIKE</div>
  <div class="abs banner-word" style="top:360px">WHEEL</div>
  <div class="abs play"><svg width="18" height="20" viewBox="0 0 18 20"><path d="M2 1l15 9-15 9z" fill="#1b1b1b"/></svg></div>
</section>

<section class="blog">
  <h2 class="abs h-section">Meet the people changing the<br>world with bikes</h2>
  <article class="post" style="left:8px;top:250px;width:292px">
    <div class="post-img" style="height:220px;background:linear-gradient(135deg,#6f8aa0,#c9b13a 50%,#3f4f2c)" role="img" aria-label="Group of riders on a sunny ride"><span class="post-tag">Friday Funday</span></div>
    <div class="post-title">Pedalon hump day cargo ride</div>
    <div class="post-meta"><span>▣ 21 AUGUST</span><span>◉ VALDORNA TEAM</span></div>
  </article>
  <article class="post" style="left:310px;top:250px;width:290px">
    <div class="post-img" style="height:220px;background:linear-gradient(135deg,#d8c7a0,#a88c58 50%,#5c5a3e)" role="img" aria-label="Cyclist on a dry hillside path"><span class="post-tag">Friday Funday</span></div>
    <div class="post-title">Alder City saves Christmas</div>
    <div class="post-meta"><span>▣ 21 AUGUST</span><span>◉ VALDORNA TEAM</span></div>
  </article>
  <article class="post" style="left:8px;top:580px;width:292px">
    <div class="post-img" style="height:220px;background:linear-gradient(135deg,#3e5a2c,#7a9a4a 50%,#2c3a22)" role="img" aria-label="Rider in a green park"><span class="post-tag">Friday Funday</span></div>
    <div class="post-title">Quality time with your loved one</div>
    <div class="post-meta"><span>▣ 21 AUGUST</span><span>◉ VALDORNA TEAM</span></div>
  </article>
  <article class="post" style="left:310px;top:580px;width:290px">
    <div class="post-img" style="height:220px;background:linear-gradient(135deg,#5a6a4a,#9a9a86 50%,#3c3e36)" role="img" aria-label="Cyclists riding through a bend"><span class="post-tag">Friday Funday</span></div>
    <div class="post-title">(Still) home of the holidays</div>
    <div class="post-meta"><span>▣ 21 AUGUST</span><span>◉ VALDORNA TEAM</span></div>
  </article>
  <article class="post big" style="left:608px;top:250px;width:584px">
    <div class="post-img" style="height:620px;background:linear-gradient(160deg,#c8cfc0,#7f8a6c 40%,#6b5a40 75%,#4a3c2a)" role="img" aria-label="Rider on a dirt path between tall trees"><span class="post-tag">Friday Funday</span></div>
    <div class="post-title">Best. Morning. Ever.</div>
    <div class="post-meta"><span>▣ 21 AUGUST</span><span>◉ VALDORNA TEAM</span></div>
  </article>
</section>

<section class="highlights" role="img" aria-label="Dark city street background">
  <div class="highlight" style="left:35px">
    <svg width="40" height="40" viewBox="0 0 40 40" fill="none" stroke="#fff" stroke-width="1.6"><path d="M8 36V6"/><path d="M8 6h24l-5 7 5 7H8"/></svg>
    <h4>TEST RIDES</h4>
    <p>Try every cargo model on our city course before you decide what suits you best</p>
  </div>
  <div class="highlight" style="left:435px">
    <svg width="40" height="40" viewBox="0 0 40 40" fill="none" stroke="#fff" stroke-width="1.6"><path d="M20 4l13 5v10c0 9-6 14-13 17C13 33 7 28 7 19V9z"/><path d="M14 20l4 4 8-9"/></svg>
    <h4>ACHIEVEMENTS</h4>
    <p>Over a thousand families advised on safe, comfortable cargo bikes for daily life</p>
  </div>
  <div class="highlight" style="left:835px">
    <svg width="40" height="40" viewBox="0 0 40 40" fill="none" stroke="#fff" stroke-width="1.6"><circle cx="20" cy="20" r="15"/><circle cx="20" cy="20" r="9"/><circle cx="20" cy="20" r="3"/></svg>
    <h4>OUR TARGETS</h4>
    <p>Greener, calmer cities where every trip can be made by bike with ease</p>
  </div>
</section>

<footer class="site-footer">
  <div class="f-col" style="left:20px">
    <h5>ABOUT US</h5>
    <p>We are a team of cargo bike consultants helping city riders choose the right bike.</p>
    <div class="socials"><span></span><span></span><span></span><span></span></div>
  </div>
  <div class="f-col" style="left:420px">
    <h5>INFORMATION</h5>
    <ul><li>Advice Sessions</li><li>Privacy Policy</li><li>Terms &amp; Conditions</li><li>Contact</li><li>Test Rides</li><li>Service</li></ul>
  </div>
  <div class="f-col" style="left:676px">
    <h5>CARGO BIKES</h5>
    <ul><li>Family Cargo</li><li>Long Tail</li><li>Electric Cargo</li><li>Compact</li><li>Accessories</li><li>Frequently Questions</li></ul>
  </div>
  <div class="f-col" style="left:916px">
    <h5>USER HELPFUL</h5>
    <ul><li>Community</li><li>Forums</li><li>Meetups</li><li>Help Center</li><li>Route Planner</li><li>Safety Tips</li></ul>
  </div>
  <div class="abs footer-bottom">
    <div class="abs footer-brand">VALDORNA</div>
    <div class="abs copyright">©2021 - Valdorna. All Right Reserved</div>
    <div class="abs footer-links"><span>Bikes</span><span>About Us</span><span>Contact</span></div>
  </div>
</footer>

</body>
</html>
```